Vellora Labs - Mushroom Supplement Packaging

Our brand is called Vellora Labs. I've added a couple different logos that you can use. We are creating a line up of Mushroom Supplement products. I will add the entire line-up of products here. I've added examples of other products and packaging shape types I can purchase. Give me different options for packaging that is minimalist and clean for this brand that makes it look really well made and clean and make people want to buy.

Product 1 Lions Mane 1g
Product 2 Cordyceps 1g
Product 3 Chaga 1g
Product 4 Turkey Tail 1g
Product 5 Reishi 1g
Product 6 Maitake 1g
Product 7 Shiitake 1g

Product 8 (Mix) Lions Mane 143mg
Cordyceps 143mg
Chaga 143mg
Turkey Tail 143mg
Reishi 143mg
Maitake 143mg
Shiitake 143mg

```html
<!DOCTYPE html>
<html lang="en">
<head>
<meta charset="UTF-8">
<title>Vellora Labs – Lion's Mane Label</title>
<link href="https://fonts.googleapis.com/css2?family=Montserrat:wght@400;500;600&family=Roboto:wght@400;500&display=swap" rel="stylesheet">
<style>
  :root {
    --page: #ffffff;
    --label-light: #e9e9ea;
    --label-mid: #dcdcdd;
    --label-dark: #d2d2d3;
    --teal: #4fb0b5;
    --teal-deep: #2f8f95;
    --ink: #2b2b2d;
    --ink-soft: #444447;
  }
  * { margin: 0; padding: 0; box-sizing: border-box; }
  html, body {
    width: 1200px;
    height: 1200px;
    overflow: hidden;
    background: var(--page);
  }
  .label {
    position: absolute;
    left: 180px;
    top: 100px;
    width: 840px;
    height: 1000px;
    background: linear-gradient(90deg, var(--label-mid) 0%, var(--label-light) 30%, var(--label-light) 60%, var(--label-dark) 100%);
  }
  .brand {
    position: absolute;
    left: 112px;
    top: 150px;
    font-family: 'Montserrat', sans-serif;
    font-weight: 600;
    font-size: 46px;
    letter-spacing: 1px;
    color: var(--ink-soft);
    text-transform: uppercase;
    line-height: 1;
  }
  .accent-rule {
    position: absolute;
    left: 116px;
    top: 391px;
    width: 3px;
    height: 527px;
    background: var(--teal);
  }
  .product-name {
    position: absolute;
    left: 133px;
    top: 384px;
    font-family: 'Roboto', sans-serif;
    font-weight: 400;
    font-size: 114px;
    letter-spacing: -1px;
    line-height: 1;
    background: linear-gradient(90deg, var(--teal) 0%, var(--teal-deep) 55%, var(--teal) 100%);
    -webkit-background-clip: text;
    background-clip: text;
    color: transparent;
    white-space: nowrap;
  }
  .benefit-line {
    position: absolute;
    left: 140px;
    top: 536px;
    font-family: 'Roboto', sans-serif;
    font-weight: 500;
    font-size: 31px;
    letter-spacing: 2px;
    color: var(--ink);
    white-space: nowrap;
  }
  .benefit-list {
    position: absolute;
    left: 142px;
    top: 668px;
    list-style: none;
    font-family: 'Montserrat', sans-serif;
    font-weight: 400;
    font-size: 22px;
    line-height: 32px;
    color: var(--ink-soft);
  }
  .benefit-list li::before { content: "- "; }
  .pack-info {
    position: absolute;
    left: 146px;
    top: 862px;
    font-family: 'Montserrat', sans-serif;
    font-weight: 500;
    font-size: 24px;
    line-height: 46px;
    color: var(--ink-soft);
    letter-spacing: 0.5px;
  }
</style>
</head>
<body>
  <section class="label">
    <div class="brand">Vellora Labs</div>
    <div class="accent-rule"></div>
    <h1 class="product-name">LION'S MANE</h1>
    <p class="benefit-line">FOCUS - CLARITY - MOOD</p>
    <ul class="benefit-list">
      <li>MEMORY</li>
      <li>FOCUS</li>
      <li>COGNITIVE BRAIN SUPPORT</li>
    </ul>
    <div class="pack-info">
      <p>60 CAPSULES</p>
      <p>DIETARY SUPPLEMENT</p>
    </div>
  </section>
</body>
</html>
```